QM Studios needs and Interior Design Business card

I can do anything from Commercial to Residential and Free lance. Beginning to end in design selection process.
Need something to catch the eye of potential customers and vendors. From furniture to Tile and Cabinet selections. I can do it all.

Industry/Entity Type

Design Agency

Contact Information for Business Card

QM Studios- Design Consultanting Residential, Commerical
Maybe a cool detail background. Wall paper print that can have some texture

Font styles to use
Serif

Colors
709dcb
34a6d7
b868aa
e667a6
f59296
85acd3
ffffff
000000
5c5c5c

Requirements
Must have
• Square or Rectangular with Rounded edges
• Name
• Address
• Phone
• Email
Nice to have
• Some colored edges More simples not too busy
• Pattern detail in background.
Should not have
• Not too much color

```html
<!DOCTYPE html>
<html lang="en">
<head>
<meta charset="utf-8">
<title>QM Studios – Business Card</title>
<link href="https://fonts.googleapis.com/css2?family=Josefin+Sans:wght@300;400&display=swap" rel="stylesheet">
<style>
  :root {
    --backdrop: #231f20;
    --cream: #f3f1e6;
    --cream-pattern: #ebe8da;
    --ink: #231f20;
    --maroon: #5e0a24;
    --rose-text: #f3e6ea;
    --rose-muted: #d6a7b4;
    --dash-light: #b9b6ab;
    --dash-dark: #b88c98;
  }
  * { margin: 0; padding: 0; box-sizing: border-box; }
  html, body { width: 1200px; height: 618px; overflow: hidden; }
  body {
    position: relative;
    background: var(--backdrop);
    font-family: "Josefin Sans", sans-serif;
    font-weight: 300;
  }
  .card {
    position: absolute;
    top: 54px;
    width: 518px;
    height: 519px;
    border-radius: 18px;
    overflow: hidden;
  }
  .card-front { left: 54px; background: var(--cream); }
  .card-back { left: 616px; background: var(--maroon); color: var(--rose-text); text-align: center; }

  .wallpaper-pattern {
    position: absolute;
    inset: 0;
    background: radial-gradient(circle at 50% 50%, var(--cream) 0%, var(--cream-pattern) 100%);
  }
  .stitch-frame {
    position: absolute;
    border: 1px dashed var(--dash-light);
    border-radius: 14px;
  }
  .card-front .stitch-frame { left: 102px; top: 100px; width: 314px; height: 316px; background: var(--cream); }
  .card-front .stitch-frame.inner { left: 106px; top: 104px; width: 306px; height: 308px; }
  .card-back .stitch-frame { left: 36px; top: 36px; width: 446px; height: 447px; border-color: var(--dash-dark); }

  .brand-name {
    position: absolute;
    left: 0; right: 0;
    top: 282px;
    text-align: center;
    font-size: 31px;
    font-weight: 400;
    letter-spacing: 4px;
    color: var(--ink);
  }
  .brand-tagline {
    position: absolute;
    left: 0; right: 0;
    top: 327px;
    text-align: center;
    font-size: 15px;
    line-height: 19px;
    color: var(--ink);
  }

  .holder-name { position: absolute; left: 0; right: 0; top: 112px; font-size: 50px; }
  .holder-title { position: absolute; left: 0; right: 0; top: 178px; font-size: 13px; color: var(--rose-muted); text-transform: uppercase; }
  .address { position: absolute; left: 0; right: 0; top: 242px; font-size: 15px; line-height: 19px; }
  .contact { position: absolute; left: 0; right: 0; top: 317px; font-size: 15px; line-height: 20px; }
  .website { position: absolute; left: 0; right: 0; top: 389px; font-size: 14px; }
</style>
</head>
<body>
  <section class="card card-front">
    <div class="wallpaper-pattern" role="img" aria-label="Soft cream wallpaper-style geometric lattice pattern"></div>
    <div class="stitch-frame"></div>
    <div class="stitch-frame inner"></div>
    <div class="brand-name">QM Studios</div>
    <div class="brand-tagline">Residential &amp; Commercial<br>Design Consulting</div>
  </section>

  <section class="card card-back">
    <div class="stitch-frame"></div>
    <div class="holder-name">Marguerite Hale</div>
    <div class="holder-title">Founder, QM Studios</div>
    <div class="address">48/2 Larkspur Avenue<br>Brookfield 402 118, NY, USA</div>
    <div class="contact">555.203.4418<br>mhale@qmstudios.com</div>
    <div class="website">www.qmstudios.com</div>
  </section>
</body>
</html>
```